Verpackungsdesign für Parfüm gesucht
Zielgruppe
Wir werden eine Marke unter dem Namen ORMAL mit Parfüm auf dem Markt bringen und benötigen hierfür ein hochwertiges Design . Unsre Zielgruppe ist m/w/d und zwischen 16 und 60 Jahre.
Aufgabenstellung
Bei der Verpackung handelt es sich um eine Schiebeschachtel. Wir benötigen das Design nur für die Außenhülle, nicht für den Schuber.
Pflichtangaben auf der Verpackung sind unser Logo, Eau de Parfum, DEEP VERDANT, 20 ml e 0.67 FL OZ,
Natural Spray Vaporisateur,

```html
<!DOCTYPE html>
<html lang="de">
<head>
<meta charset="utf-8">
<title>ORMAL – Deep Verdant Eau de Parfum</title>
<link href="https://fonts.googleapis.com/css2?family=Montserrat:wght@300;700&display=swap" rel="stylesheet">
<style>
  :root {
    --sleeve-teal: #124840;
    --sleeve-teal-deep: #0e3d36;
    --sleeve-top: #161616;
    --brand-silver: #d8dedc;
    --label-light: #e2e8e6;
    --label-muted: #3d6a63;
    --volume-grey: #6f8f89;
  }
  * { margin: 0; padding: 0; box-sizing: border-box; }
  html, body {
    width: 800px;
    height: 1200px;
    overflow: hidden;
  }
  body {
    font-family: "Montserrat", Arial, sans-serif;
  }
  .sleeve-front {
    position: relative;
    width: 800px;
    height: 1200px;
    background: linear-gradient(180deg,
      var(--sleeve-top) 0%,
      var(--sleeve-teal-deep) 9%,
      var(--sleeve-teal) 30%,
      var(--sleeve-teal) 100%);
    text-align: center;
  }
  .brand-name {
    position: absolute;
    top: 225px;
    left: 0;
    right: 0;
    font-weight: 300;
    font-size: 120px;
    letter-spacing: 12px;
    padding-left: 12px;
    color: var(--brand-silver);
    line-height: 1;
  }
  .product-info {
    position: absolute;
    top: 795px;
    left: 0;
    right: 0;
  }
  .edition {
    font-weight: 700;
    font-size: 26px;
    letter-spacing: 1.5px;
    color: var(--label-light);
    margin-bottom: 34px;
  }
  .fragrance-type {
    font-weight: 700;
    font-size: 19px;
    letter-spacing: 1px;
    line-height: 1.3;
    color: var(--label-muted);
    text-transform: uppercase;
  }
  .volume {
    font-weight: 700;
    font-size: 28px;
    letter-spacing: 1px;
    color: var(--volume-grey);
    margin-top: 24px;
  }
</style>
</head>
<body>
  <main class="sleeve-front">
    <h1 class="brand-name">ORMAL</h1>
    <section class="product-info">
      <p class="edition">DEEP VERDANT</p>
      <p class="fragrance-type">Eau de Parfum<br>Natural Spray Vaporisateur</p>
      <p class="volume">20 ml ℮ 0.67 FL OZ</p>
    </section>
  </main>
</body>
</html>
```